Dorian's Roam Almanac Mobile App

We need a sleek new design for our new mobile app we are launching in the South Pacific. This app will be released for both iPhone and Android. The app has already been developed and your new design will give it the finishing touch we need to release it to our audience. This will be the premiere tourism app for the South Pacific and will be advertised heavily in our successful print publications which are distributed internationally. We are looking for you to provide two designs (for two screens in our mobile app) for this competition. The selected winner will have the opportunity to design the remaining screens in our app and website as a separate contract.

Attached you will see a few of the screens that currently exist in our mobile app to give you a feel for the functionality. The two screens we want you to design for this competition are the main listing page and the category selection page. These two screens will be included in the uploaded files and will be clearly marked so you know what we are looking for.

Please feel free to reach out to us with any questions if you need any guidance in directing your designs. Show us something sleek, engaging, and ultimately something that will drive our users to want to engage with the businesses that are listed in the app.

Please see the uploaded files for a couple of our current designs, the two screens we want you to design for this competition, and a few samples of design ideas we like.

Best of Luck!

Target Market(s)

Travelers to the South Pacific

Industry/Entity Type

Travel Industry

Font styles to use
Serif
Sans Serif

Colors
0492cd
33a6d7
ec1f27
f04a50
85cae6
cee9f5
f59296
cedeed
fbd4d5

Requirements
Must have
• Clean, attractive design for the two screens mentioned in the brief.
Nice to have
• Icon sets, color guide, font selection
Should not have
• Project should not be too busy or incorporate too many different colors, styles, fonts, etc.

```html
<!DOCTYPE html>
<html lang="en">
<head>
<meta charset="utf-8">
<title>Dorian's Roam Almanac – App Screens</title>
<link href="https://fonts.googleapis.com/css2?family=Montserrat:wght@600;700&family=Quicksand:wght@400;500;600&display=swap" rel="stylesheet">
<style>
  :root{
    --navy:#1b5a7d;
    --coral:#f2552c;
    --coral-soft:#ff7a59;
    --ice:#b4d8df;
    --paper:#ffffff;
    --mist:#f3f4f4;
    --ink:#3a3a3a;
    --ink-soft:#8a8a8a;
    --line:#e3e3e3;
  }
  *{box-sizing:border-box;margin:0;padding:0}
  html,body{width:1200px;height:1055px;overflow:hidden}
  body{background:var(--navy);font-family:"Quicksand",sans-serif;color:var(--ink);position:relative}

  .brand{position:absolute;top:50px;left:0;width:1200px;display:flex;justify-content:center;align-items:center;gap:14px}
  .brand-dot{width:22px;height:22px;border-radius:50%;background:var(--paper)}
  .brand-name{font-family:"Montserrat",sans-serif;font-weight:600;font-size:40px;color:var(--paper);letter-spacing:-.5px}

  .screen{position:absolute;top:266px;width:368px;height:654px;overflow:hidden;background:var(--paper)}
  .screen-home{left:168px;background:var(--ice)}
  .screen-details{left:670px;background:var(--mist)}

  .status{position:absolute;top:0;left:0;right:0;height:24px;display:flex;align-items:center;justify-content:space-between;padding:0 14px 0 18px;font-family:"Montserrat",sans-serif;font-weight:600;font-size:12px;z-index:3}
  .status-time{position:absolute;left:0;right:0;text-align:center}
  .status-right{display:flex;align-items:center;gap:4px}
  .batt{width:24px;height:10px;border-radius:2px}
  .screen-home .status{color:#111}
  .screen-home .batt{background:#111}
  .screen-details .status{color:var(--paper)}
  .screen-details .batt{background:var(--paper)}

  /* home */
  .hero{position:absolute;top:0;left:0;width:368px;height:310px;background:linear-gradient(180deg,#8fc4e8 0%,#dbeaf2 28%,#6cc7c6 48%,#4fc1c0 62%,#a9dcd9 82%,var(--ice) 100%)}
  .welcome{position:absolute;top:96px;left:0;right:0;text-align:center;font-family:"Montserrat",sans-serif;font-weight:700;font-size:24px;line-height:30px;letter-spacing:1px;color:var(--coral)}
  .island-label{position:absolute;top:251px;left:29px;font-size:11.5px;color:#333}
  .island-select{position:absolute;top:269px;left:24px;width:320px;height:30px;background:var(--paper);border-radius:3px;box-shadow:0 1px 3px rgba(0,0,0,.15);display:flex;align-items:center;padding:0 12px 0 12px;font-size:12px;gap:8px}
  .island-select .caret{margin-left:auto}

  .category-grid{position:absolute;top:331px;left:7px;display:grid;grid-template-columns:repeat(3,113px);grid-auto-rows:101px;column-gap:8px;row-gap:18px}
  .category{background:var(--paper);border-radius:2px;box-shadow:0 1px 3px rgba(0,0,0,.18);display:flex;flex-direction:column;align-items:center;justify-content:flex-end;padding-bottom:16px;gap:10px;font-size:12.5px;font-weight:500;color:#333}
  .category svg{width:40px;height:36px;stroke:var(--coral);fill:none;stroke-width:1.6;stroke-linecap:round;stroke-linejoin:round}

  .tabbar{position:absolute;left:0;right:0;height:46px;background:var(--paper);display:grid;grid-template-columns:repeat(4,1fr);align-items:center;text-align:center;font-size:10px;font-family:"Montserrat",sans-serif;color:#444}
  .screen-home .tabbar{top:608px}
  .screen-details .tabbar{top:610px;border-top:1px solid var(--line)}
  .tab{display:flex;flex-direction:column;align-items:center;gap:2px;font-weight:400}
  .tab svg{width:20px;height:20px;fill:none;stroke:#888;stroke-width:1.4}
  .tab.is-active{color:var(--navy)}
  .tab.is-active svg{fill:var(--navy);stroke:var(--navy)}

  /* details */
  .appbar{position:absolute;top:0;left:0;right:0;height:73px;background:var(--navy)}
  .appbar-title{position:absolute;top:38px;left:0;right:0;text-align:center;font-family:"Montserrat",sans-serif;font-weight:600;font-size:16px;color:var(--paper)}
  .appbar-back{position:absolute;top:38px;left:10px;width:14px;height:22px;fill:none;stroke:var(--paper);stroke-width:1.5}
  .listing-photo{position:absolute;top:73px;left:0;width:368px;height:280px;background:linear-gradient(160deg,#d8d2c6 0%,#9b8f80 40%,#6c6257 70%,#3c3834 100%)}
  .listing-name{position:absolute;top:289px;left:15px;font-family:"Montserrat",sans-serif;font-weight:700;font-size:22px;letter-spacing:.5px;color:var(--paper)}
  .rating{position:absolute;top:324px;left:16px;display:flex;gap:2px}
  .rating svg{width:20px;height:20px}
  .listing-actions{position:absolute;top:292px;left:290px;display:flex;gap:18px}
  .listing-actions svg{width:22px;height:22px;fill:none;stroke:var(--paper);stroke-width:1.5}
  .pager{position:absolute;top:341px;left:173px;display:flex;gap:3px;align-items:center}
  .pager i{width:6px;height:6px;border-radius:50%;border:1px solid var(--paper)}
  .pager i.on{background:var(--paper);width:8px;height:8px}

  .segments{position:absolute;top:353px;left:0;right:0;height:38px;background:var(--paper);display:flex;font-size:18px;color:#9a9a9a;padding-left:0}
  .segment{padding:0 0 0 0;display:flex;align-items:center;justify-content:center;height:100%}
  .segment.is-active{color:var(--coral);border-bottom:2px solid var(--coral)}
  .seg-1{width:124px}.seg-2{width:94px}.seg-3{width:150px}

  .description{position:absolute;top:408px;left:15px;width:340px;font-size:12.4px;line-height:17.4px;color:#444;font-weight:500}
  .btn{position:absolute;top:559px;width:132px;height:34px;border-radius:17px;background:var(--coral);color:var(--paper);font-family:"Montserrat",sans-serif;font-weight:600;font-size:11.5px;letter-spacing:.5px;display:flex;align-items:center;justify-content:center;box-shadow:0 2px 3px rgba(0,0,0,.2)}
  .btn-rate{left:41px}
  .btn-review{left:187px}
</style>
</head>
<body>

<header class="brand">
  <span class="brand-dot"></span>
  <span class="brand-name">Dorian's Roam Almanac</span>
</header>

<!-- Home / category selection -->
<section class="screen screen-home">
  <div class="hero" role="img" aria-label="Photo of a turquoise lagoon with palm-covered island, boat and cloudy sky"></div>
  <div class="status">
    <span>●●●○○</span>
    <span class="status-time">4:21 PM</span>
    <span class="status-right">100% <span class="batt"></span></span>
  </div>
  <h1 class="welcome">WELCOME TO<br>COOK'S ISLANDS!</h1>
  <p class="island-label">Select an Island...</p>
  <div class="island-select">
    <svg width="12" height="16" viewBox="0 0 12 16"><path d="M6 0a6 6 0 0 0-6 6c0 4.5 6 10 6 10s6-5.5 6-10a6 6 0 0 0-6-6z" fill="#f2552c"/><circle cx="6" cy="6" r="2.2" fill="#fff"/></svg>
    <span>- Rarotonga -</span>
    <svg class="caret" width="20" height="11" viewBox="0 0 20 11"><path d="M0 0h20L10 11z" fill="#333"/></svg>
  </div>

  <div class="category-grid">
    <div class="category">
      <svg viewBox="0 0 40 36"><rect x="4" y="6" width="32" height="12" rx="2"/><rect x="8" y="11" width="10" height="7" rx="2"/><rect x="22" y="11" width="10" height="7" rx="2"/><rect x="2" y="18" width="36" height="10"/><path d="M4 28v4M36 28v4M2 22h36"/></svg>
      Accomodation
    </div>
    <div class="category">
      <svg viewBox="0 0 40 36"><rect x="3" y="6" width="34" height="20" rx="3"/><path d="M3 13h34M11 6v7M19 6v7M27 6v7M3 20h34"/><circle cx="11" cy="28" r="3"/><circle cx="29" cy="28" r="3"/></svg>
      Transportation
    </div>
    <div class="category">
      <svg viewBox="0 0 40 36"><circle cx="8" cy="6" r="3"/><circle cx="32" cy="6" r="3"/><path d="M4 12v12h8v8M36 12v12h-8v8M10 18h20v14M20 10v8M16 10v3M24 10v4"/></svg>
      Food &amp; Drink
    </div>
    <div class="category">
      <svg viewBox="0 0 40 36"><path d="M6 26C8 12 18 4 24 2c-2 8-4 18-8 26z"/><circle cx="29" cy="10" r="3"/><path d="M26 14l-6 10M2 30c4-3 6 3 10 0s6 3 10 0 6 3 10 0 6 3 6 0"/></svg>
      Activities
    </div>
    <div class="category">
      <svg viewBox="0 0 40 36"><rect x="3" y="7" width="34" height="22" rx="2"/><path d="M14 7v22M3 16h20M20 24h4M27 24h4M10 16c-3-4 0-6 4 0 4-6 7-4 4 0"/></svg>
      Coupons
    </div>
    <div class="category">
      <svg viewBox="0 0 40 36"><path d="M20 32S4 22 4 12a8 8 0 0 1 16-2 8 8 0 0 1 16 2c0 10-16 20-16 20z"/></svg>
      Favourites
    </div>
  </div>

  <nav class="tabbar">
    <span class="tab is-active"><svg viewBox="0 0 20 20"><path d="M2 10L10 2l8 8v8h-5v-5H7v5H2z"/></svg>HOME</span>
    <span class="tab"><svg viewBox="0 0 20 20"><circle cx="8" cy="8" r="6"/><path d="M12.5 12.5L18 18"/></svg>SEARCH</span>
    <span class="tab"><svg viewBox="0 0 20 20"><path d="M4 1h8l4 4v6M4 1v18h8M12 1v4h4"/><path d="M15 12l1.2 2.4 2.6.4-1.9 1.8.5 2.6-2.4-1.3-2.4 1.3.5-2.6-1.9-1.8 2.6-.4z"/></svg>SAVED</span>
    <span class="tab"><svg viewBox="0 0 20 20"><circle cx="10" cy="10" r="9"/><circle cx="10" cy="8" r="3.5"/><path d="M4 16c2-4 10-4 12 0"/></svg>ME</span>
  </nav>
</section>

<!-- Listing details -->
<section class="screen screen-details">
  <div class="appbar"></div>
  <div class="status">
    <span>●●●○○</span>
    <span class="status-time">4:21 PM</span>
    <span class="status-right">100% <span class="batt"></span></span>
  </div>
  <svg class="appbar-back" viewBox="0 0 14 22"><path d="M12 1L2 11l10 10"/></svg>
  <h2 class="appbar-title">DETAILS</h2>

  <div class="listing-photo" role="img" aria-label="Photo of a bright hotel lounge with sofas, bookshelves and a view to the pool"></div>
  <h3 class="listing-name">LAGOON LODGE</h3>
  <div class="rating">
    <svg viewBox="0 0 20 20"><path d="M10 1l2.7 5.9 6.3.6-4.8 4.3 1.4 6.3L10 14.8 4.4 18.1l1.4-6.3L1 7.5l6.3-.6z" fill="#f2552c"/></svg>
    <svg viewBox="0 0 20 20"><path d="M10 1l2.7 5.9 6.3.6-4.8 4.3 1.4 6.3L10 14.8 4.4 18.1l1.4-6.3L1 7.5l6.3-.6z" fill="#f2552c"/></svg>
    <svg viewBox="0 0 20 20"><path d="M10 1l2.7 5.9 6.3.6-4.8 4.3 1.4 6.3L10 14.8 4.4 18.1l1.4-6.3L1 7.5l6.3-.6z" fill="#f2552c"/></svg>
    <svg viewBox="0 0 20 20"><path d="M10 1l2.7 5.9 6.3.6-4.8 4.3 1.4 6.3L10 14.8 4.4 18.1l1.4-6.3L1 7.5l6.3-.6z" fill="#f2552c"/></svg>
    <svg viewBox="0 0 20 20"><path d="M10 1l2.7 5.9 6.3.6-4.8 4.3 1.4 6.3L10 14.8 4.4 18.1l1.4-6.3L1 7.5l6.3-.6z" fill="none" stroke="#f2552c" stroke-width="1.3"/><path d="M10 1v13.8L4.4 18.1l1.4-6.3L1 7.5l6.3-.6z" fill="#f2552c"/></svg>
  </div>
  <div class="listing-actions">
    <svg viewBox="0 0 22 22"><path d="M11 20S2 14 2 7.5a4.8 4.8 0 0 1 9-2.3 4.8 4.8 0 0 1 9 2.3C20 14 11 20 11 20z"/></svg>
    <svg viewBox="0 0 22 22"><path d="M4 1h9l4 4v6M4 1v20h9M13 1v4h4"/><path d="M17 13l1.2 2.4 2.6.4-1.9 1.8.5 2.6-2.4-1.3-2.4 1.3.5-2.6-1.9-1.8 2.6-.4z"/></svg>
  </div>
  <div class="pager"><i></i><i class="on"></i><i></i></div>

  <div class="segments">
    <span class="segment seg-1 is-active">Description</span>
    <span class="segment seg-2">Contact</span>
    <span class="segment seg-3">Map/Direction</span>
  </div>

  <p class="description">Lagoon Lodge is lorem ipsum dolor sit amet, consectetur adipisicing elit, sed do eiusmod tempor incididunt ut labore et dolore magna aliqua. Ut enim ad minim veniam, quis nostrud exercitation ullamco laboris nisi ut aliquip ex ea commodo consequat. Duis aute irure dolor in reprehenderit in voluptate velit esse cillum dolore eu fugiat nulla pariatur. Excepteur sint occaecat cupidatat non proident,</p>

  <span class="btn btn-rate">RATE IT</span>
  <span class="btn btn-review">READ REVIEW</span>

  <nav class="tabbar">
    <span class="tab is-active"><svg viewBox="0 0 20 20"><path d="M2 10L10 2l8 8v8h-5v-5H7v5H2z"/></svg>HOME</span>
    <span class="tab"><svg viewBox="0 0 20 20"><circle cx="8" cy="8" r="6"/><path d="M12.5 12.5L18 18"/></svg>SEARCH</span>
    <span class="tab"><svg viewBox="0 0 20 20"><path d="M4 1h8l4 4v6M4 1v18h8M12 1v4h4"/><path d="M15 12l1.2 2.4 2.6.4-1.9 1.8.5 2.6-2.4-1.3-2.4 1.3.5-2.6-1.9-1.8 2.6-.4z"/></svg>SAVED</span>
    <span class="tab"><svg viewBox="0 0 20 20"><circle cx="10" cy="10" r="9"/><circle cx="10" cy="8" r="3.5"/><path d="M4 16c2-4 10-4 12 0"/></svg>ME</span>
  </nav>
</section>

</body>
</html>
```